2019/20 Season Calendar (This is to be at the top of the calendar as title)

An advertising calendar for our agricultural business to explain our key business attributes and give clients a nice looking calendar to refer to .

Please refer to doc/pdf attachments for text details and ideas. (Our current logo needs to be incorporated - this logo can be altered if need be)

open to professional agriculture aesthetics keeping in line with the companies Green colour scheme (logo)

The calendar is to start at October 2019 - September 2020

97mm x 122mm

Target Market(s)

Agricultural sector (professional)

Industry/Entity Type

Agriculture

Font styles to use
Sans Serif

Colors
abd036
3276b5

Requirements
Must have
• Calender with dates starting october 1st 2019 finishing end of september 2020.
• Must include all public holidays etc for Australia during this time.
• contact details including website :www.brevittholdings.com.au
Nice to have
• In the calendar the months of
• October/ nov /december (be coloured yellow)
• April/May/June (be coloured brown)
• July /aug/september (be coloured green)
• Jan/feb/march (be coloured white)
• Then in the corner of the calendar a key (like a map) to refer to the colours
• [a small square with the colour yellow] (next to the square the following text) Harvesting
• [a small square with the colour brown] (next to the square the following text) Sowing
• [a small square with the colour green] (next to the square the following text) Growing
• [a small square with the colour white] (next to the square the following text) Liming + Fertilising

```html
<!DOCTYPE html>
<html lang="en">
<head>
<meta charset="utf-8">
<title>2019/20 Season Calendar – Brevitt Holdings</title>
<link rel="stylesheet" href="https://fonts.googleapis.com/css2?family=Arimo:wght@700&family=Montserrat:wght@400;500;700;800&display=swap">
<style>
  :root{
    --brand-green:#abd036;
    --brand-blue:#3276b5;
    --body-dark:#2b2b2b;
    --title-brown:#472a28;
    --logo-green:#16813a;
    --ink:#2f2f2f;
    --holiday:#d8221c;
    --season-liming:#c7c7c7;
    --season-sowing:#9c6a0c;
    --season-growing:#12bf12;
    --season-harvest:#c9b81c;
    --key-harvest:#f4e40e;
    --key-sowing:#a06a10;
    --key-growing:#10c010;
    --key-liming:#ffffff;
  }
  *{box-sizing:border-box;margin:0;padding:0}
  html,body{width:1200px;height:960px;overflow:hidden;background:#fff}
  body{font-family:"Montserrat",sans-serif;position:relative}

  .calendar{position:absolute;left:245px;top:71px;width:711px;height:822px;background:var(--body-dark);overflow:hidden}

  .hero{position:absolute;left:0;top:0;width:711px;height:215px;
    background:linear-gradient(180deg,#b1c2d8 0%,#c3cdd6 45%,#8f9b78 50%,#bfcf2a 56%,#cfdc2e 100%)}
  .hero-band{position:absolute;left:0;top:215px;width:711px;height:8px;background:var(--brand-green)}
  .title{position:absolute;left:0;top:28px;width:711px;text-align:center;
    font-family:"Arimo",sans-serif;font-weight:700;font-size:37px;color:var(--title-brown);letter-spacing:.3px}

  .logo-tab{position:absolute;left:261px;top:153px;width:209px;height:66px;background:var(--brand-green);
    border-radius:26px 26px 0 0;display:flex;align-items:center;justify-content:center;gap:7px}
  .logo-tab .mark{width:14px;height:14px;background:var(--logo-green)}
  .logo-tab .name{font-weight:800;font-size:15px;color:var(--logo-green);letter-spacing:.4px}

  .stripe-top{position:absolute;left:521px;top:223px;width:200px;height:13px;background:var(--brand-blue);
    transform:skewX(40deg);transform-origin:top left}
  .stripe-bottom{position:absolute;left:-10px;top:773px;width:196px;height:9px;background:var(--brand-blue);
    transform:skewX(50deg);transform-origin:bottom left}

  .month{position:absolute;width:183px;height:123px}
  .month.liming{background:var(--season-liming)}
  .month.sowing{background:var(--season-sowing)}
  .month.growing{background:var(--season-growing)}
  .month.harvest{background:var(--season-harvest)}
  .month-name{position:absolute;left:22px;top:1px;width:141px;height:21px;background:var(--brand-blue);
    border-radius:7px;color:#fff;font-weight:700;font-size:17px;line-height:21px;text-align:center;letter-spacing:.5px}
  .days{position:absolute;left:6px;top:24px;display:grid;grid-template-columns:repeat(7,24.4px);
    grid-auto-rows:16.6px;font-size:12.5px;color:var(--ink);text-align:center;line-height:16.6px}
  .days .head{color:#555;font-weight:500}
  .days .hol{color:var(--holiday)}

  .col1{left:30px}.col2{left:266px}.col3{left:501px}
  .row1{top:240px}.row2{top:371px}.row3{top:500px}.row4{top:630px}

  .key{position:absolute;left:187px;top:760px;display:flex;gap:12px;align-items:center;color:#e6e6e6;font-size:13.5px}
  .key-item{display:flex;align-items:center;gap:6px}
  .swatch{width:32px;height:12px}

  .footer-left{position:absolute;left:0;top:782px;width:352px;height:40px;background:var(--brand-green)}
  .footer-right{position:absolute;left:355px;top:782px;width:356px;height:40px;background:var(--brand-blue)}
  .contact{position:absolute;display:flex;align-items:flex-start;gap:4px;color:#fff;font-size:10px;line-height:12.5px}
  .contact svg{flex:none;margin-top:1px}
  .address{left:49px;top:6px}
  .phone{left:215px;top:6px}
  .web{left:437px;top:6px}
</style>
</head>
<body>
<main class="calendar">
  <div class="hero" role="img" aria-label="Aerial photo of flowering canola fields with scattered gum trees under a pale sky"></div>
  <div class="hero-band"></div>
  <h1 class="title">2019/20 SEASON CALENDAR</h1>
  <div class="logo-tab"><span class="mark"></span><span class="name">BREVITT HOLDINGS</span></div>
  <div class="stripe-top"></div>

  <section class="month liming col1 row1"><h2 class="month-name">JANUARY</h2>
    <div class="days"><b class="head">S</b><b class="head">M</b><b class="head">T</b><b class="head">W</b><b class="head">T</b><b class="head">F</b><b class="head">S</b>
      <i></i><i></i><span class="hol">1</span><span>2</span><span>3</span><span>4</span><span>5</span>
      <span>6</span><span>7</span><span>8</span><span>9</span><span>10</span><span>11</span><span>12</span>
      <span>13</span><span>14</span><span>15</span><span>16</span><span>17</span><span>18</span><span>19</span>
      <span>20</span><span>21</span><span>22</span><span>23</span><span>24</span><span class="hol">26</span><span>27</span>
      <span>28</span><span>29</span><span>30</span><span>31</span></div></section>

  <section class="month liming col2 row1"><h2 class="month-name">FEBRUARY</h2>
    <div class="days"><b class="head">S</b><b class="head">M</b><b class="head">T</b><b class="head">W</b><b class="head">T</b><b class="head">F</b><b class="head">S</b>
      <i></i><i></i><i></i><i></i><span>1</span><span>2</span><span>3</span>
      <span>4</span><span>5</span><span>6</span><span>7</span><span>8</span><span>9</span><span>10</span>
      <span>11</span><span>12</span><span>13</span><span>14</span><span>15</span><span>16</span><span>17</span>
      <span>18</span><span>19</span><span>20</span><span>21</span><span>22</span><span>23</span><span>24</span>
      <span>25</span><span>26</span><span>27</span><span>28</span></div></section>

  <section class="month liming col3 row1"><h2 class="month-name">MARCH</h2>
    <div class="days"><b class="head">S</b><b class="head">M</b><b class="head">T</b><b class="head">W</b><b class="head">T</b><b class="head">F</b><b class="head">S</b>
      <i></i><i></i><i></i><i></i><span>1</span><span>2</span><span>3</span>
      <span>4</span><span class="hol">5</span><span>6</span><span>7</span><span>8</span><span>9</span><span>10</span>
      <span>11</span><span>12</span><span>13</span><span>14</span><span>15</span><span>16</span><span>17</span>
      <span>18</span><span>19</span><span>20</span><span>21</span><span>22</span><span>23</span><span>24</span>
      <span>25</span><span>26</span><span>27</span><span>28</span><span>29</span><span class="hol">30</span><span>31</span></div></section>

  <section class="month sowing col1 row2"><h2 class="month-name">APRIL</h2>
    <div class="days"><b class="head">S</b><b class="head">M</b><b class="head">T</b><b class="head">W</b><b class="head">T</b><b class="head">F</b><b class="head">S</b>
      <span>1</span><span class="hol">2</span><span>3</span><span>4</span><span>5</span><span>6</span><span>7</span>
      <span>8</span><span>9</span><span>10</span><span>11</span><span>12</span><span>13</span><span>14</span>
      <span>15</span><span>16</span><span>17</span><span>18</span><span>19</span><span>20</span><span>21</span>
      <span>22</span><span>23</span><span>24</span><span class="hol">25</span><span>26</span><span>27</span><span>28</span>
      <span>29</span><span>30</span></div></section>

  <section class="month sowing col2 row2"><h2 class="month-name">MAY</h2>
    <div class="days"><b class="head">S</b><b class="head">M</b><b class="head">T</b><b class="head">W</b><b class="head">T</b><b class="head">F</b><b class="head">S</b>
      <i></i><i></i><span>1</span><span>2</span><span>3</span><span>4</span><span>5</span>
      <span>6</span><span>7</span><span>8</span><span>9</span><span>10</span><span>11</span><span>12</span>
      <span>13</span><span>14</span><span>15</span><span>16</span><span>17</span><span>18</span><span>19</span>
      <span>20</span><span>21</span><span>22</span><span>23</span><span>24</span><span>25</span><span>26</span>
      <span>27</span><span>28</span><span>29</span><span>30</span><span>31</span></div></section>

  <section class="month sowing col3 row2"><h2 class="month-name">JUNE</h2>
    <div class="days"><b class="head">S</b><b class="head">M</b><b class="head">T</b><b class="head">W</b><b class="head">T</b><b class="head">F</b><b class="head">S</b>
      <i></i><i></i><i></i><i></i><i></i><span>1</span><span>2</span>
      <span>3</span><span class="hol">4</span><span>5</span><span>6</span><span>7</span><span>8</span><span>9</span>
      <span>10</span><span>11</span><span>12</span><span>13</span><span>14</span><span>15</span><span>16</span>
      <span>17</span><span>18</span><span>19</span><span>20</span><span>21</span><span>22</span><span>23</span>
      <span>24</span><span>25</span><span>26</span><span>27</span><span>28</span><span>29</span><span>30</span></div></section>

  <section class="month growing col1 row3"><h2 class="month-name">JULY</h2>
    <div class="days"><b class="head">S</b><b class="head">M</b><b class="head">T</b><b class="head">W</b><b class="head">T</b><b class="head">F</b><b class="head">S</b>
      <span>1</span><span>2</span><span>3</span><span>4</span><span>5</span><span>6</span><span>7</span>
      <span>8</span><span>9</span><span>10</span><span>11</span><span>12</span><span>13</span><span>14</span>
      <span>15</span><span>16</span><span>17</span><span>18</span><span>19</span><span>20</span><span>21</span>
      <span>22</span><span>23</span><span>24</span><span>25</span><span>26</span><span>27</span><span>28</span>
      <span>29</span><span>30</span><span>31</span></div></section>

  <section class="month growing col2 row3"><h2 class="month-name">AUGUST</h2>
    <div class="days"><b class="head">S</b><b class="head">M</b><b class="head">T</b><b class="head">W</b><b class="head">T</b><b class="head">F</b><b class="head">S</b>
      <i></i><i></i><i></i><span>1</span><span>2</span><span>3</span><span>4</span>
      <span>5</span><span>6</span><span>7</span><span>8</span><span>9</span><span>10</span><span>11</span>
      <span>12</span><span>13</span><span>14</span><span>15</span><span>16</span><span>17</span><span>18</span>
      <span>19</span><span>20</span><span>21</span><span>22</span><span>23</span><span>24</span><span>25</span>
      <span>26</span><span>27</span><span>28</span><span>29</span><span>30</span><span>31</span></div></section>

  <section class="month growing col3 row3"><h2 class="month-name">SEPTEMBER</h2>
    <div class="days"><b class="head">S</b><b class="head">M</b><b class="head">T</b><b class="head">W</b><b class="head">T</b><b class="head">F</b><b class="head">S</b>
      <span>30</span><i></i><i></i><i></i><i></i><i></i><span>1</span>
      <span>2</span><span>3</span><span>4</span><span>5</span><span>6</span><span>7</span><span>8</span>
      <span>9</span><span>10</span><span>11</span><span>12</span><span>13</span><span>14</span><span>15</span>
      <span>16</span><span>17</span><span>18</span><span>19</span><span>20</span><span>21</span><span>22</span>
      <span>23</span><span class="hol">24</span><span>25</span><span>26</span><span>27</span><span>28</span><span>29</span></div></section>

  <section class="month harvest col1 row4"><h2 class="month-name">OCTOBER</h2>
    <div class="days"><b class="head">S</b><b class="head">M</b><b class="head">T</b><b class="head">W</b><b class="head">T</b><b class="head">F</b><b class="head">S</b>
      <i></i><span>1</span><span>2</span><span>3</span><span>4</span><span>5</span><span>6</span>
      <span>7</span><span>8</span><span>9</span><span>10</span><span>11</span><span>12</span><span>13</span>
      <span>14</span><span>15</span><span>16</span><span>17</span><span>18</span><span>19</span><span>20</span>
      <span>21</span><span>22</span><span>23</span><span>24</span><span>25</span><span>26</span><span>27</span>
      <span>28</span><span>29</span><span>30</span><span>31</span></div></section>

  <section class="month harvest col2 row4"><h2 class="month-name">NOVEMBER</h2>
    <div class="days"><b class="head">S</b><b class="head">M</b><b class="head">T</b><b class="head">W</b><b class="head">T</b><b class="head">F</b><b class="head">S</b>
      <i></i><i></i><i></i><i></i><span>1</span><span>2</span><span>3</span>
      <span>4</span><span>5</span><span>6</span><span>7</span><span>8</span><span>9</span><span>10</span>
      <span>11</span><span>12</span><span>13</span><span>14</span><span>15</span><span>16</span><span>17</span>
      <span>18</span><span>19</span><span>20</span><span>21</span><span>22</span><span>23</span><span>24</span>
      <span>25</span><span>26</span><span>27</span><span>28</span><span>29</span><span>30</span></div></section>

  <section class="month harvest col3 row4"><h2 class="month-name">DECEMBER</h2>
    <div class="days"><b class="head">S</b><b class="head">M</b><b class="head">T</b><b class="head">W</b><b class="head">T</b><b class="head">F</b><b class="head">S</b>
      <span>30</span><span>31</span><i></i><i></i><i></i><i></i><span>1</span>
      <span>2</span><span>3</span><span>4</span><span>5</span><span>6</span><span>7</span><span>8</span>
      <span>9</span><span>10</span><span>11</span><span>12</span><span>13</span><span>14</span><span>15</span>
      <span>16</span><span>17</span><span>18</span><span>19</span><span>20</span><span>21</span><span>22</span>
      <span>23</span><span>24</span><span class="hol">25</span><span class="hol">26</span><span>27</span><span>28</span><span>29</span></div></section>

  <div class="key">
    <div class="key-item"><span class="swatch" style="background:var(--key-harvest)"></span>Harvesting</div>
    <div class="key-item"><span class="swatch" style="background:var(--key-sowing)"></span>Sowing</div>
    <div class="key-item"><span class="swatch" style="background:var(--key-growing)"></span>Growing</div>
    <div class="key-item"><span class="swatch" style="background:var(--key-liming)"></span>Liming + Fertilising</div>
  </div>

  <div class="stripe-bottom"></div>
  <div class="footer-left"></div>
  <div class="footer-right"></div>

  <div class="contact address">
    <svg width="12" height="12" viewBox="0 0 12 12"><circle cx="6" cy="6" r="6" fill="#fff"/><path d="M6 2.5a2.2 2.2 0 0 0-2.2 2.2C3.8 6.4 6 9.3 6 9.3s2.2-2.9 2.2-4.6A2.2 2.2 0 0 0 6 2.5z" fill="#abd036"/><circle cx="6" cy="4.7" r=".8" fill="#fff"/></svg>
    <span>14 Wattle Road,<br>Coolamon NSW 2701, Australia</span>
  </div>
  <div class="contact phone">
    <svg width="12" height="12" viewBox="0 0 12 12"><circle cx="6" cy="6" r="6" fill="#fff"/><path d="M4.2 3c.3 0 .5.1.6.4l.4 1c.1.2 0 .5-.2.6l-.4.3c.4.8 1 1.4 1.8 1.8l.3-.4c.2-.2.4-.3.6-.2l1 .4c.3.1.4.3.4.6v.8c0 .4-.3.7-.7.7C5.6 9 3 6.4 3 3.7 3 3.3 3.3 3 3.7 3z" fill="#abd036"/></svg>
    <span>02-6900-4512</span>
  </div>
  <div class="contact web">
    <svg width="12" height="12" viewBox="0 0 12 12"><circle cx="6" cy="6" r="5.4" fill="none" stroke="#fff" stroke-width="1.1"/><ellipse cx="6" cy="6" rx="2.3" ry="5.4" fill="none" stroke="#fff" stroke-width=".9"/><path d="M.8 6h10.4M1.8 3.4h8.4M1.8 8.6h8.4" stroke="#fff" stroke-width=".8"/></svg>
    <span>www.brevittholdings.com.au</span>
  </div>
</main>
</body>
</html>
```